Business Card - connecting 2 souls and beggining the journey of self discovery

Logo on the front
with tag line

On the back list of services and contact details

Seminars
workshops
Coaching
podcasts

Darren Whitlow
Health & Wellbeing Life Coach
0468 215 937
darren@wearebrightroots.net
wearebrightroots.net

Industry/Entity Type

Life Coaching

Contact Information for Business Card

I like the use of colour from the logo to be used. I'm not a fan of white.

Requirements
Must have
• My tagline: Every bright path begins within
Nice to have
• Use of colour that is in the mind body soul logo

```html
<!DOCTYPE html>
<html lang="en">
<head>
<meta charset="utf-8">
<title>Bright Roots Wellbeing – Business Cards</title>
<link rel="stylesheet" href="https://fonts.googleapis.com/css2?family=Open+Sans:wght@400;600;700&display=swap">
<style>
  :root {
    --backdrop: #3a2f2a;
    --card: #141516;
    --card-edge: #1d1e20;
    --teal: #4fc7a0;
    --pink: #f0577a;
    --ink: #f2f2f2;
    --muted: #9a9c9f;
    --brand-grey: #8d8f92;
    --circle-dark: #2a2b2d;
    --circle-light: #55575a;
  }
  * { box-sizing: border-box; margin: 0; padding: 0; }
  html, body {
    width: 1200px; height: 864px; overflow: hidden;
    background: var(--backdrop);
    font-family: "Open Sans", Arial, sans-serif;
  }
  .canvas { position: relative; width: 1200px; height: 864px; }

  .card {
    position: absolute;
    width: 540px; height: 330px;
    background: var(--card);
    border: 1px solid var(--card-edge);
    border-radius: 4px;
    box-shadow: 0 18px 40px rgba(0,0,0,.45);
  }
  .card--front { left: 50px; top: 110px; }
  .card--back { left: 610px; top: 424px; }

  /* Front */
  .front-mark {
    position: absolute; left: 190px; top: 56px;
    display: flex; flex-direction: column; align-items: center; gap: 14px;
  }
  .front-mark__circle {
    width: 140px; height: 140px; border-radius: 50%;
    background: radial-gradient(circle at 35% 30%, var(--circle-light), var(--circle-dark) 75%);
  }
  .front-mark__name {
    color: var(--muted); font-size: 15px; font-weight: 600; letter-spacing: .04em;
  }
  .services {
    position: absolute; left: 38px; bottom: 46px;
    color: var(--muted); font-size: 15px; font-weight: 400;
    display: flex; align-items: center; gap: 8px;
  }
  .services .dot { width: 5px; height: 5px; border-radius: 50%; background: var(--teal); }

  /* Back */
  .identity { position: absolute; left: 34px; top: 112px; }
  .identity__name {
    color: var(--teal); font-size: 17px; font-weight: 700; letter-spacing: .02em; text-transform: uppercase;
  }
  .identity__role {
    color: var(--pink); font-size: 17px; font-weight: 600; letter-spacing: .02em; text-transform: uppercase;
    margin-top: 2px;
  }
  .contact { list-style: none; margin-top: 12px; }
  .contact li {
    display: flex; align-items: center; gap: 8px;
    color: var(--ink); font-size: 14.5px; line-height: 22px;
  }
  .contact svg { width: 12px; height: 12px; fill: var(--teal); flex: none; }
  .rule {
    position: absolute; left: 34px; right: 30px; top: 262px;
    height: 1px; background: var(--teal); opacity: .8;
  }
  .brand {
    position: absolute; right: 30px; top: 112px;
    display: flex; flex-direction: column; align-items: flex-start;
  }
  .brand__circle {
    width: 56px; height: 56px; border-radius: 50%;
    background: linear-gradient(135deg, #f05b8a, #b65fd0 40%, #f6b64a 75%, #6fd39c);
    margin-left: 88px; margin-bottom: 8px;
  }
  .brand__name { color: var(--brand-grey); font-size: 20px; font-weight: 600; letter-spacing: -.01em; }
  .brand__tagline { color: var(--brand-grey); font-size: 13px; font-weight: 600; margin-top: 1px; }
</style>
</head>
<body>
<main class="canvas">
  <section class="card card--front" aria-label="Business card front">
    <div class="front-mark">
      <div class="front-mark__circle"></div>
      <p class="front-mark__name">Bright Roots Wellbeing</p>
    </div>
    <p class="services">
      <span>Seminars</span><span class="dot"></span>
      <span>Workshops</span><span class="dot"></span>
      <span>Coaching</span><span class="dot"></span>
      <span>Podcasts</span>
    </p>
  </section>

  <section class="card card--back" aria-label="Business card back">
    <div class="identity">
      <h1 class="identity__name">Darren Whitlow</h1>
      <h2 class="identity__role">Health &amp; Wellbeing Life Coach</h2>
      <ul class="contact">
        <li>
          <svg viewBox="0 0 24 24" aria-hidden="true"><path d="M6.6 10.8a15.1 15.1 0 0 0 6.6 6.6l2.2-2.2a1 1 0 0 1 1-.25 11.4 11.4 0 0 0 3.6.57 1 1 0 0 1 1 1V20a1 1 0 0 1-1 1A17 17 0 0 1 3 4a1 1 0 0 1 1-1h3.5a1 1 0 0 1 1 1c0 1.25.2 2.45.57 3.57a1 1 0 0 1-.25 1z"/></svg>
          0468 215 937
        </li>
        <li>
          <svg viewBox="0 0 24 24" aria-hidden="true"><path d="M2 5h20v14H2z M2 5l10 8 10-8" stroke="#141516" stroke-width="1.5"/></svg>
          darren@wearebrightroots.net
        </li>
        <li>
          <svg viewBox="0 0 24 24" aria-hidden="true"><path d="M12 2a7 7 0 0 0-7 7c0 5 7 13 7 13s7-8 7-13a7 7 0 0 0-7-7zm0 9.5A2.5 2.5 0 1 1 12 6.5a2.5 2.5 0 0 1 0 5z"/></svg>
          www.wearebrightroots.net
        </li>
      </ul>
    </div>
    <div class="brand">
      <div class="brand__circle"></div>
      <p class="brand__name">Bright Roots Wellbeing</p>
      <p class="brand__tagline">Every bright path begins within</p>
    </div>
    <div class="rule"></div>
  </section>
</main>
</body>
</html>
```